Gymnastics Award Design Needed--for kids

Need a gymnastics certificate or award designed. Will be printed on a piece of 8.5x11 paper. The award will be celebrating the gymnast learning a new skill in gymnastics. So it should be fun, but still look "official". Needs to look good hanging on a gymnast's bedroom wall.

It should say "The Aerial Cartwheel Club"
I will be using this design to change it based on the skill.

My main colors are:
#34475D
#E1467A
#7555A4

So should use those, but can add others

My website is tumblenestpro.com so you can see the look/feel.

Target Market(s)

Main audience will be girls ages 5-12, but will also be used by slightly older girls and boys. So needs to be fun, not too gender specific.

Industry/Entity Type

Learning

Requirements
Must have
• The following will need to go on the certificate:
• * Name of Skill
• * Image of Skill
• * Gymnast's Name
• * my logo
• * Gym's Logo
• * Gym's Name
• Optional: Date

```html
<!DOCTYPE html>
<html lang="en">
<head>
<meta charset="utf-8">
<title>The Aerial Cartwheel Club – Award Certificate</title>
<link rel="stylesheet" href="https://fonts.googleapis.com/css2?family=Patrick+Hand&family=PT+Sans:wght@400&display=swap">
<style>
  :root {
    --page-bg: #ececec;
    --red: #e42a2a;
    --orange: #ea6a24;
    --yellow: #fde513;
    --green: #16a04a;
    --navy: #213a8c;
    --purple: #7a3392;
    --border-gold: #f8cc0f;
    --panel: #ffffff;
    --ink: #1b1b1b;
    --name-ink: #23318c;
    --dots: #2c55b5;
    --ribbon: #7555a4;
    --brand-pink: #e1467a;
    --bubble-blue: #c9e4f6;
    --bubble-pink: #f8d6e0;
    --bubble-yellow: #fbf6c4;
  }
  * { margin: 0; padding: 0; box-sizing: border-box; }
  html, body { width: 1200px; height: 940px; overflow: hidden; background: var(--page-bg); }

  .certificate {
    position: absolute;
    left: 30px; top: 64px;
    width: 1140px; height: 812px;
    background: repeating-linear-gradient(135deg,
      var(--red) 0 80px, var(--orange) 80px 160px, var(--yellow) 160px 240px,
      var(--green) 240px 320px, var(--navy) 320px 400px, var(--purple) 400px 480px);
    overflow: hidden;
    font-family: "Patrick Hand", cursive;
    color: var(--ink);
  }
  .panel-shape { position: absolute; inset: 0; filter: drop-shadow(4px 6px 4px rgba(0,0,0,.3)); }

  .bubble { position: absolute; border-radius: 50%; opacity: .85; }
  .bubble--a { left: 296px; top: 106px; width: 78px; height: 78px; background: var(--bubble-blue); }
  .bubble--b { left: 210px; top: 364px; width: 150px; height: 150px; background: var(--bubble-yellow); }
  .bubble--c { left: 90px; top: 452px; width: 56px; height: 56px; background: var(--bubble-blue); }
  .bubble--d { left: 132px; top: 588px; width: 116px; height: 116px; background: var(--bubble-pink); }
  .bubble--e { left: 728px; top: 156px; width: 104px; height: 104px; background: var(--bubble-pink); }
  .bubble--f { left: 942px; top: 306px; width: 74px; height: 74px; background: var(--bubble-blue); }
  .bubble--g { left: 840px; top: 452px; width: 170px; height: 170px; background: var(--bubble-blue); }
  .bubble--h { left: 726px; top: 604px; width: 46px; height: 46px; background: var(--bubble-yellow); }
  .bubble--i { left: 834px; top: 692px; width: 20px; height: 20px; background: var(--bubble-pink); }

  .ribbon { position: absolute; left: 469px; top: 0; width: 204px; height: 203px; }
  .crown-emblem {
    position: absolute; left: 529px; top: 38px; width: 84px; height: 62px;
    background: var(--border-gold); border-radius: 6px;
  }

  .illustration { position: absolute; border-radius: 40px; }
  .illustration--left {
    left: 111px; top: 115px; width: 200px; height: 252px;
    background: radial-gradient(ellipse at center, #f6a93a 0%, #fbd9b6 55%, rgba(255,255,255,0) 75%);
  }
  .illustration--right {
    left: 795px; top: 147px; width: 226px; height: 233px;
    background: radial-gradient(ellipse at center, #7a3d9a 0%, #7fbde8 50%, rgba(255,255,255,0) 75%);
  }

  .text { position: absolute; text-align: center; white-space: nowrap; }
  .presented-to { left: 0; width: 1146px; top: 229px; font-size: 32px; letter-spacing: .5px; }
  .recipient {
    left: 0; width: 1140px; top: 314px;
    font-family: "PT Sans", sans-serif; font-size: 46px; color: var(--name-ink);
  }
  .dotted-line { position: absolute; border-top: 3px dotted var(--dots); }
  .dotted-line--name { left: 356px; width: 433px; top: 362px; }
  .recognition { left: 0; width: 1154px; top: 394px; font-size: 30px; line-height: 40px; }

  .by-star { position: absolute; left: 530px; top: 482px; width: 94px; height: 90px; }
  .by-label { left: 530px; width: 94px; top: 508px; font-size: 32px; color: var(--name-ink); }

  .date-value { left: 130px; width: 219px; top: 576px; font-family: "PT Sans", sans-serif; font-size: 20px; }
  .dotted-line--date { left: 130px; width: 219px; top: 611px; }
  .date-label { left: 130px; width: 222px; top: 620px; font-size: 24px; }

  .brand { position: absolute; left: 372px; top: 590px; display: flex; align-items: center; gap: 12px; }
  .brand-dot { width: 26px; height: 26px; border-radius: 50%; background: var(--ribbon); }
  .brand-name { font-size: 40px; color: var(--brand-pink); letter-spacing: 1px; }

  .dotted-line--signature { left: 788px; width: 222px; top: 611px; }
  .signature-label { left: 788px; width: 222px; top: 620px; font-size: 24px; }
</style>
</head>
<body>
<main class="certificate">
  <svg class="panel-shape" width="1140" height="812" viewBox="0 0 1140 812" aria-hidden="true">
    <path d="M62 72 C250 50 420 90 600 66 S900 58 1082 70 C1096 250 1070 420 1088 560 S1078 700 1086 738 C900 752 780 722 600 740 S250 760 70 742 C52 600 80 450 60 300 S70 120 62 72 Z"
          fill="var(--panel)" stroke="var(--border-gold)" stroke-width="12" stroke-linejoin="round"/>
  </svg>

  <span class="bubble bubble--a"></span>
  <span class="bubble bubble--b"></span>
  <span class="bubble bubble--c"></span>
  <span class="bubble bubble--d"></span>
  <span class="bubble bubble--e"></span>
  <span class="bubble bubble--f"></span>
  <span class="bubble bubble--g"></span>
  <span class="bubble bubble--h"></span>
  <span class="bubble bubble--i"></span>

  <svg class="ribbon" viewBox="0 0 204 203" aria-hidden="true">
    <path d="M0 0 H204 V203 L102 140 L0 203 Z" fill="var(--ribbon)"/>
    <rect x="12" y="0" width="10" height="190" fill="var(--border-gold)"/>
    <rect x="182" y="0" width="10" height="190" fill="var(--border-gold)"/>
  </svg>
  <div class="crown-emblem" role="img" aria-label="Gold crown emblem"></div>

  <div class="illustration illustration--left" role="img" aria-label="Illustration of a gymnast performing an aerial cartwheel on a beam"></div>
  <div class="illustration illustration--right" role="img" aria-label="Illustration of a rhythmic gymnast dancing with a ribbon"></div>

  <p class="text presented-to">PRESENTED TO</p>
  <p class="text recipient">Maya Ellison</p>
  <div class="dotted-line dotted-line--name"></div>
  <p class="text recognition">FOR LEARNING THE AERIAL CARTWHEEL AND JOINING<br>THE AERIAL CARTWHEEL CLUB</p>

  <svg class="by-star" viewBox="0 0 94 90" aria-hidden="true">
    <polygon points="47,2 59,32 92,34 66,55 75,88 47,70 19,88 28,55 2,34 35,32" fill="var(--yellow)" stroke="var(--border-gold)" stroke-width="3" stroke-linejoin="round"/>
  </svg>
  <p class="text by-label">By</p>

  <p class="text date-value">00/00/2017</p>
  <div class="dotted-line dotted-line--date"></div>
  <p class="text date-label">DATE</p>

  <div class="brand">
    <span class="brand-dot"></span>
    <span class="brand-name">TUMBLENEST PRO</span>
  </div>

  <div class="dotted-line dotted-line--signature"></div>
  <p class="text signature-label">SIGNATURE</p>
</main>
</body>
</html>
```